Anesthesia Medical Practice Business Card

We need a business card to hand out to surgeons with my basic information. Something that stands out but is not over the top. The medical community is rather conservative. I'd like them to call me first when flipping through their rolodex of anesthesiologists. I'd like the card to communicate confidence, control, professionalism yet serenity. I don't want the card to be pricey to print.

he logo will be provided as a vector graphic in addition to a complete business card design including the logo

Rex Alba Tovell, M.D.
Board Certified Anesthesiologist

(555) 638-2175

rtovell@quillnet.example

Mailing Address:
48317 Pemberly Ave.
Suite 274-6583
Los Angeles, CA 90871

A logo that inegrates my initials perhaps
RT MD
My initials are RT and MD as in Medical Doctor

or
perhaps a physician in surgical mask and cap caring for a patient

Surgeons who need anesthesia services

Medical

• the logo will be provided as a vector graphic in addition to a complete business card design including the logo

Rex Alba Tovell, M.D.

(555) 638-2175

rtovell@quillnet.example

Mailing Address:
48317 Pemberly Ave.
Suite 274-6583
Los Angeles, CA 90871

• A logo that inegrates my initials perhaps
RT MD

or

```html
<!DOCTYPE html>
<html lang="en">
<head>
<meta charset="utf-8">
<title>Rex Alba Tovell, M.D. — Business Card</title>
<link rel="stylesheet" href="https://fonts.googleapis.com/css2?family=Didact+Gothic&family=Montserrat:wght@700&display=swap">
<style>
  :root {
    --accent: #e0522a;
    --ink: #39434a;
    --card: #ffffff;
    --backdrop: #e8e6e3;
    --card-shadow: rgba(0, 0, 0, 0.12);
  }
  * { box-sizing: border-box; margin: 0; padding: 0; }
  html, body {
    width: 1200px;
    height: 1000px;
    overflow: hidden;
    background: var(--backdrop);
  }
  .sheet {
    position: relative;
    width: 1200px;
    height: 1000px;
  }
  .card {
    position: absolute;
    left: 250px;
    width: 700px;
    height: 400px;
    background: var(--card);
    border-radius: 28px;
    box-shadow: 0 6px 20px var(--card-shadow);
    font-family: "Didact Gothic", "Century Gothic", sans-serif;
    color: var(--ink);
  }
  .card--front { top: 70px; }
  .card--back  { top: 530px; }

  /* Front */
  .front-mark {
    position: absolute;
    left: 0; right: 0;
    top: 120px;
    text-align: center;
  }
  .front-mark__name {
    display: block;
    font-size: 88px;
    line-height: 1;
    letter-spacing: 4px;
    color: var(--ink);
  }
  .front-mark__role {
    display: block;
    margin-top: 14px;
    font-size: 42px;
    line-height: 1;
    color: var(--ink);
  }

  /* Back */
  .identity {
    position: absolute;
    left: 56px;
    top: 46px;
  }
  .identity__name {
    font-family: "Montserrat", "Century Gothic", sans-serif;
    font-weight: 700;
    font-size: 27px;
    color: var(--accent);
    line-height: 1.1;
  }
  .identity__title {
    font-size: 21px;
    line-height: 1.2;
    margin-top: 2px;
  }
  .back-mark {
    position: absolute;
    right: 90px;
    top: 96px;
    font-size: 48px;
    letter-spacing: 3px;
    line-height: 1;
    color: var(--ink);
  }
  .address {
    position: absolute;
    left: 56px;
    top: 196px;
    font-size: 21px;
    line-height: 1.25;
    font-style: normal;
  }
  .address__label {
    color: var(--accent);
    display: block;
  }
  .contact {
    position: absolute;
    left: 430px;
    top: 272px;
    list-style: none;
    font-size: 21px;
  }
  .contact__item {
    display: flex;
    align-items: center;
    gap: 14px;
    height: 28px;
    margin-bottom: 20px;
  }
  .contact__icon {
    width: 16px;
    height: 16px;
    flex: none;
  }
</style>
</head>
<body>
<main class="sheet">

  <section class="card card--front" aria-label="Card front">
    <div class="front-mark">
      <span class="front-mark__name">RT MD</span>
      <span class="front-mark__role">Anesthesiologist</span>
    </div>
  </section>

  <section class="card card--back" aria-label="Card back">
    <header class="identity">
      <h1 class="identity__name">Rex Alba Tovell, M.D.</h1>
      <p class="identity__title">Board Certified Anesthesiologist</p>
    </header>

    <div class="back-mark">RT MD</div>

    <address class="address">
      <span class="address__label">Mailing Address:</span>
      48317 Pemberly Ave.<br>
      Suite 274-6583<br>
      Los Angeles, CA 90871
    </address>

    <ul class="contact">
      <li class="contact__item">
        <svg class="contact__icon" viewBox="0 0 16 16" aria-hidden="true">
          <rect x="4" y="1" width="8" height="14" rx="1.5" fill="none" stroke="var(--accent)" stroke-width="1.6"/>
          <line x1="7" y1="12.5" x2="9" y2="12.5" stroke="var(--accent)" stroke-width="1.4"/>
        </svg>
        <span>(555) 638-2175</span>
      </li>
      <li class="contact__item">
        <svg class="contact__icon" viewBox="0 0 16 16" aria-hidden="true">
          <rect x="1" y="3" width="14" height="10" fill="none" stroke="var(--accent)" stroke-width="1.5"/>
          <polyline points="1,3 8,9 15,3" fill="none" stroke="var(--accent)" stroke-width="1.5"/>
          <polyline points="1,13 6,7.5 M10,7.5 15,13" fill="none" stroke="var(--accent)" stroke-width="1.2"/>
        </svg>
        <span>rtovell@quillnet.example</span>
      </li>
    </ul>
  </section>

</main>
</body>
</html>
```